Figure for a research paper

I am working on designing a figure for a research paper that illustrates the effect of KADO Pathways assessment on student outcomes over time by impacting teacher bias and teacher perception of student growth. I built the attached figure via powerpoint. It includes the very basic elements but it does not look great and I am not sure that it is clearly depicting what I am hoping to illustrate. I would like for you to build an illustration of this idea that i can include in the paper.

```html
<!DOCTYPE html>
<html lang="en">
<head>
<meta charset="utf-8">
<title>Assessment effect on SEL program effectiveness over time</title>
<link href="https://fonts.googleapis.com/css2?family=Source+Sans+3:wght@400&display=swap" rel="stylesheet">
<style>
  :root {
    --navy: #183562;
    --ink: #17355f;
    --axis-wall: #98acca;
    --floor: #c8c9ce;
    --card: #f2f2f0;
    --card-edge: #d9dad9;
    --trend-base: #dfe9e8;
    --trend-boost: #e8312f;
    --label: #c9cbd0;
  }
  html, body {
    margin: 0;
    width: 1200px;
    height: 1200px;
    overflow: hidden;
    background: var(--navy);
  }
  .figure-sheet {
    display: block;
    width: 1200px;
    height: 1200px;
    font-family: "Source Sans 3", "Myriad Pro", sans-serif;
  }
  .fig-label { fill: var(--label); font-size: 70px; }
  .axis-wall { fill: var(--axis-wall); }
  .axis-floor { fill: var(--floor); }
  .axis-title { fill: var(--ink); font-size: 22px; }
  .card-body { fill: var(--card); }
  .card-edge { fill: var(--card-edge); }
  .card-text { fill: var(--ink); font-size: 23px; text-anchor: middle; }
  .arrow { fill: var(--card); stroke: var(--card-edge); stroke-width: 3; stroke-linejoin: round; }
  .trend-base { stroke: var(--trend-base); stroke-width: 15; }
  .trend-boost { stroke: var(--trend-boost); stroke-width: 17; }
</style>
</head>
<body>
<svg class="figure-sheet" viewBox="0 0 1932 1932" xmlns="http://www.w3.org/2000/svg">
  <defs>
    <linearGradient id="area-fade" x1="0" y1="0" x2="0" y2="1">
      <stop offset="0" stop-color="#1d3a68"/>
      <stop offset="1" stop-color="#35507e"/>
    </linearGradient>
  </defs>

  <!-- Figure 1 -->
  <g class="chart chart-baseline">
    <text class="fig-label" x="268" y="336">FIg. 1</text>
    <polygon points="614,598 1311,493 1311,682 614,682" fill="url(#area-fade)"/>
    <rect class="axis-wall" x="538" y="184" width="76" height="590"/>
    <polygon class="axis-floor" points="538,774 614,682 1393,682 1393,774"/>
    <text class="axis-title" x="970" y="728" text-anchor="middle">Time</text>
    <text class="axis-title" transform="translate(584 449) rotate(-90)" text-anchor="middle">Effectiveness of SEL Program on the Student</text>
    <line class="trend-base" x1="614" y1="598" x2="1333" y2="490"/>

    <g class="factor factor-bias">
      <rect class="card-edge" x="675" y="360" width="290" height="112"/>
      <rect class="card-body" x="680" y="360" width="285" height="107"/>
      <text class="card-text" x="823" y="424">Teacher Bias</text>
      <polygon class="arrow" points="720,469 740,469 740,518 772,518 729,565 686,518 720,518"/>
      <polygon class="arrow" points="898,469 918,469 918,490 949,490 906,537 863,490 898,490"/>
    </g>

    <g class="factor factor-perception">
      <rect class="card-edge" x="1061" y="310" width="290" height="112"/>
      <rect class="card-body" x="1066" y="310" width="285" height="107"/>
      <text class="card-text" x="1203" y="346">Teacher’s inaccurate</text>
      <text class="card-text" x="1203" y="373">perception of student</text>
      <text class="card-text" x="1203" y="400">growth (or learning)</text>
      <polygon class="arrow" points="1108,419 1128,419 1128,463 1158,463 1115,510 1072,463 1108,463"/>
      <polygon class="arrow" points="1285,419 1305,419 1305,438 1335,438 1292,486 1249,438 1285,438"/>
    </g>
  </g>

  <!-- Figure 2 -->
  <g class="chart chart-with-assessment">
    <text class="fig-label" x="268" y="1133">FIg. 2</text>
    <polygon points="614,1533 1311,1430 1311,1616 614,1616" fill="url(#area-fade)"/>
    <rect class="axis-wall" x="538" y="1044" width="76" height="664"/>
    <polygon class="axis-floor" points="538,1708 614,1616 1520,1616 1520,1708"/>
    <text class="axis-title" x="970" y="1662" text-anchor="middle">Time</text>
    <text class="axis-title" transform="translate(584 1382) rotate(-90)" text-anchor="middle">Effectiveness of SEL Program on the Student</text>
    <line class="trend-base" x1="614" y1="1533" x2="1090" y2="1462"/>
    <line class="trend-boost" x1="614" y1="1516" x2="1357" y2="1226"/>

    <g class="factor factor-bias">
      <rect class="card-edge" x="682" y="1208" width="290" height="113"/>
      <rect class="card-body" x="687" y="1208" width="285" height="108"/>
      <text class="card-text" x="831" y="1271">Teacher Bias</text>
      <polygon class="arrow" points="727,1318 747,1318 747,1406 779,1406 736,1453 693,1406 727,1406"/>
      <polygon class="arrow" points="906,1318 926,1318 926,1338 957,1338 914,1385 871,1338 906,1338"/>
    </g>

    <g class="factor factor-perception">
      <rect class="card-edge" x="1026" y="1074" width="290" height="113"/>
      <rect class="card-body" x="1031" y="1074" width="285" height="108"/>
      <text class="card-text" x="1168" y="1110">Teacher’s inaccurate</text>
      <text class="card-text" x="1168" y="1137">perception of student</text>
      <text class="card-text" x="1168" y="1164">growth (or learning)</text>
      <polygon class="arrow" points="1072,1184 1092,1184 1092,1270 1122,1270 1079,1317 1036,1270 1072,1270"/>
      <polygon class="arrow" points="1250,1184 1270,1184 1270,1205 1300,1205 1257,1251 1214,1205 1250,1205"/>
    </g>

    <g class="factor factor-assessment">
      <polygon class="arrow" points="1135,1388 1155,1388 1155,1371 1190,1371 1147,1324 1104,1371 1135,1371"/>
      <polygon class="arrow" points="1314,1388 1334,1388 1334,1305 1368,1305 1325,1256 1282,1305 1314,1305"/>
      <rect class="card-edge" x="1088" y="1386" width="290" height="112"/>
      <rect class="card-body" x="1088" y="1391" width="285" height="107"/>
      <text class="card-text" x="1226" y="1437">KADO Pathways</text>
      <text class="card-text" x="1226" y="1464">Assessment</text>
    </g>
  </g>
</svg>
</body>
</html>
```